Byte Lantern Website

Design and implement (fully coded and ready to launch) website for a professional services company - please see the documents attached and send us an email if there are any questions
Target Market(s)
Market to potential clients about the services we offer and be able to reach us for any consulting opportunities
Industry/Entity Type
Professional Service
Coding
Coded - Design and coding required
Number of Pages Required
3 page
Requirements
Must have
- Single page website design that is SEO optimized
Blog Post
Contact US page
Cool images/ logos for the service offering - not fill the website with text/content
Must be professional looking website
Coded website should also look great on different screens - mobile, tablets etc
Nice to have
- Choose easy neutral colors that compliment the logo colors. Having said that don't use every color in the logo for the website design.
Should not have
- Too many colors and several various different fonts

```html
<!DOCTYPE html>
<html lang="en">
<head>
<meta charset="utf-8">
<title>Byte Lantern – Home Page Concept</title>
<link rel="stylesheet" href="https://fonts.googleapis.com/css2?family=Poppins:wght@400;500;600;700;800&display=swap">
<style>
:root{
  --orange:#f37324;
  --orange-deep:#ec6a1c;
  --ink:#111111;
  --text:#222222;
  --muted:#6b6b6b;
  --paper:#fdf7f6;
  --white:#ffffff;
  --line:#e6e6e6;
  --footer:#000000;
  --footer-bar:#121212;
  --violet:#7b4fb3;
  --blue:#2d5fc4;
}
*{box-sizing:border-box;margin:0;padding:0}
html,body{width:1200px;height:2974px;overflow:hidden}
body{background:var(--paper);font-family:"Poppins",sans-serif;color:var(--text);position:relative}
.abs{position:absolute}
.brand-band{position:absolute;left:0;top:0;width:1200px;height:747px;background:var(--orange)}
.brand-name{position:absolute;left:0;width:1200px;top:100px;text-align:center;color:var(--white);font-weight:500;font-size:28px;letter-spacing:2px}
.brand-dot{display:inline-block;width:22px;height:22px;border:3px solid var(--white);border-radius:50%;vertical-align:-3px;margin-right:10px}
.board-title{position:absolute;left:0;width:1200px;top:188px;text-align:center;color:var(--white);font-weight:800;font-size:56px;letter-spacing:1px}

.site{position:absolute;background:var(--white);overflow:hidden}
.nav{position:absolute;left:0;top:0;width:100%;background:var(--white)}
.logo{position:absolute;font-weight:600;color:var(--text);white-space:nowrap}
.logo i{display:inline-block;border:2px solid var(--orange);border-radius:50%;vertical-align:middle;margin-right:5px}
.nav-link{position:absolute;font-size:8px;color:#444}
.nav-link.active::before{content:"";position:absolute;left:0;right:0;top:-17px;height:3px;background:var(--orange)}
.social{position:absolute;width:8px;height:8px;background:var(--blue);border-radius:1px}
.mail-btn{position:absolute;width:26px;height:26px;border-radius:50%;background:var(--orange);box-shadow:0 0 0 3px #f9c7a5}
.mail-btn::after{content:"";position:absolute;left:9px;top:10px;width:8px;height:6px;background:var(--white);border-radius:1px}
.hero{position:absolute;left:0;width:100%;background:linear-gradient(135deg,var(--orange) 0%,var(--orange-deep) 100%)}
.hero-title{position:absolute;color:var(--white);font-weight:800;line-height:1.08;white-space:nowrap}
.hero-text{position:absolute;color:var(--white)}
.accent{position:absolute;border-radius:3px;background:var(--orange)}
.accent.light{background:var(--white)}
.btn{position:absolute;background:var(--white);color:var(--orange);font-weight:500;display:flex;align-items:center;justify-content:center}
.section-title{position:absolute;color:var(--ink);font-weight:800;line-height:1.2;white-space:nowrap}
.section-text{position:absolute;color:var(--text);line-height:1.45}
.arrow{position:absolute;border-radius:50%;background:var(--orange);box-shadow:0 0 0 3px #fbd6bf}
.arrow svg{position:absolute;left:0;top:0;width:100%;height:100%}
.partner{position:absolute;color:#333;font-weight:600;text-align:center}
.partner-sep{position:absolute;width:1px;background:#d9d9d9}
.card{position:absolute;background:var(--white);box-shadow:0 2px 8px rgba(0,0,0,.12)}
.card-icon{position:absolute;border-radius:8px;background:linear-gradient(135deg,var(--violet),var(--blue))}
.card-title{position:absolute;font-weight:600;color:#222;white-space:nowrap}
.card-text{position:absolute;color:var(--muted);line-height:1.5}
.post{position:absolute;background:var(--white);box-shadow:0 2px 8px rgba(0,0,0,.12);overflow:hidden}
.post-img{position:absolute;left:0;top:0;width:100%}
.post-date{position:absolute;color:var(--muted)}
.post-title{position:absolute;font-weight:500;color:#222;white-space:nowrap}
.footer{position:absolute;left:0;width:100%;background:var(--footer);color:var(--white)}
.foot-head{position:absolute;font-weight:600;color:var(--white)}
.foot-link{position:absolute;color:#cfcfcf}
.field{position:absolute;border-bottom:1px solid #444;color:#777}
.foot-bar{position:absolute;left:0;width:100%;background:var(--footer-bar)}
.round{position:absolute;border-radius:50%}
.divider{position:absolute;height:1px;background:#333}
</style>
</head>
<body>

<div class="brand-band"></div>
<div class="brand-name"><span class="brand-dot"></span>BYTE LANTERN</div>
<div class="board-title">Home Page Concept</div>

<!-- desktop hero preview -->
<div class="site" style="left:241px;top:346px;width:716px;height:450px">
  <div class="nav" style="height:56px">
    <div class="logo" style="left:88px;top:20px;font-size:11px"><i style="width:10px;height:10px"></i>BYTE LANTERN</div>
    <div class="nav-link active" style="left:292px;top:22px">Home</div>
    <div class="nav-link" style="left:341px;top:22px">Services</div>
    <div class="nav-link" style="left:401px;top:22px">Blogs</div>
    <div class="social" style="left:563px;top:24px"></div>
    <div class="social" style="left:575px;top:24px"></div>
    <div class="mail-btn" style="left:611px;top:15px"></div>
  </div>
  <div class="hero" style="top:56px;height:394px">
    <div class="hero-title" style="left:88px;top:76px;font-size:48px">Welcome To<br>Byte Lantern LLC</div>
    <div class="accent light" role="img" aria-label="Wavy accent line" style="left:88px;top:222px;width:66px;height:6px"></div>
    <div class="hero-text" style="left:173px;top:208px;font-size:11.5px;width:440px;line-height:1.25">Lorem ipsum dolor sit amet, consectetur adipiscing elit, sed do eiusmod tempor incididunt ut labore et dolore magna aliqua.</div>
    <div class="btn" style="left:90px;top:262px;width:84px;height:26px;font-size:7px">Contact Us</div>
  </div>
</div>

<!-- phone services preview -->
<div class="site" style="left:862px;top:512px;width:160px;height:360px">
  <div class="arrow" style="left:8px;top:24px;width:12px;height:12px"></div>
  <div class="partner" style="left:40px;top:22px;width:80px;font-size:9px">Streamline</div>
  <div class="arrow" style="left:140px;top:24px;width:12px;height:12px"></div>
  <div class="section-title" style="left:6px;top:75px;font-size:13.5px">Byte Lantern LLC<br>Services</div>
  <div class="accent" role="img" aria-label="Wavy accent line" style="left:7px;top:146px;width:36px;height:4px"></div>
  <div class="section-text" style="left:62px;top:136px;font-size:8px;width:92px">Lorem ipsum dolor sit amet, consectetur adipiscing...</div>
  <div class="card" style="left:10px;top:194px;width:140px;height:114px">
    <div class="card-icon" role="img" aria-label="Cloud development illustration" style="left:12px;top:14px;width:26px;height:26px"></div>
    <div class="card-title" style="left:12px;top:50px;font-size:9px">Cloud Development</div>
    <div class="card-text" style="left:12px;top:68px;font-size:6px;width:116px">Byte Lantern works very closely with clients, product...</div>
  </div>
  <div class="card" style="left:10px;top:318px;width:140px;height:60px">
    <div class="card-icon" role="img" aria-label="Data engineering illustration" style="left:12px;top:12px;width:26px;height:26px"></div>
  </div>
</div>

<div class="divider" style="left:375px;top:955px;width:202px"></div>
<div class="round" style="left:594px;top:949px;width:12px;height:12px;background:#222"></div>
<div class="divider" style="left:623px;top:955px;width:202px"></div>

<!-- mobile home page -->
<div class="site" style="left:113px;top:1043px;width:167px;height:1743px">
  <div class="nav" style="height:32px">
    <div class="logo" style="left:8px;top:10px;font-size:6px"><i style="width:6px;height:6px"></i>BYTE LANTERN</div>
    <svg class="abs" style="left:148px;top:12px" width="10" height="8" viewBox="0 0 10 8"><path d="M0 1h10M0 4h10M0 7h10" stroke="#f37324" stroke-width="1.2"/></svg>
  </div>
  <div class="hero" style="top:32px;height:271px">
    <div class="hero-title" style="left:9px;top:72px;font-size:14.5px">Welcome To<br>Byte Lantern LLC</div>
    <div class="accent light" role="img" aria-label="Wavy accent line" style="left:9px;top:154px;width:34px;height:4px"></div>
    <div class="hero-text" style="left:53px;top:132px;font-size:7px;width:108px;line-height:1.2">Lorem ipsum dolor sit amet, consectetur adipiscing elit, sed do eiusmod tempor incididunt ut labore et dolore magna aliqua.</div>
    <div class="btn" style="left:9px;top:207px;width:62px;height:19px;font-size:5.5px">Contact Us</div>
  </div>
  <div class="arrow" style="left:11px;top:342px;width:12px;height:12px"></div>
  <div class="partner" style="left:44px;top:341px;width:80px;font-size:9px">Streamline</div>
  <div class="arrow" style="left:144px;top:342px;width:12px;height:12px"></div>

  <div class="section-title" style="left:8px;top:392px;font-size:14px">Byte Lantern LLC<br>Services</div>
  <div class="accent" role="img" aria-label="Wavy accent line" style="left:9px;top:464px;width:36px;height:4px"></div>
  <div class="section-text" style="left:66px;top:450px;font-size:8px;width:95px">Lorem ipsum dolor sit amet, consectetur adipiscing...</div>

  <div class="card" style="left:9px;top:510px;width:150px;height:110px">
    <div class="card-icon" role="img" aria-label="Cloud development illustration" style="left:12px;top:14px;width:26px;height:26px"></div>
    <div class="card-title" style="left:12px;top:52px;font-size:8.5px">Cloud Development</div>
    <div class="card-text" style="left:12px;top:72px;font-size:5.5px;width:118px">Byte Lantern works very closely with clients, product...</div>
  </div>
  <div class="card" style="left:9px;top:629px;width:150px;height:110px">
    <div class="card-icon" role="img" aria-label="Data engineering illustration" style="left:12px;top:14px;width:26px;height:26px"></div>
    <div class="card-title" style="left:12px;top:52px;font-size:8.5px">Cloud Development</div>
    <div class="card-text" style="left:12px;top:72px;font-size:5.5px;width:118px">Byte Lantern works very closely with clients, product...</div>
  </div>
  <div class="card" style="left:9px;top:748px;width:150px;height:110px">
    <div class="card-icon" role="img" aria-label="Cloud development illustration" style="left:12px;top:14px;width:26px;height:26px"></div>
    <div class="card-title" style="left:12px;top:52px;font-size:8.5px">Cloud Development</div>
    <div class="card-text" style="left:12px;top:72px;font-size:5.5px;width:118px">Byte Lantern works very closely with clients, product...</div>
  </div>

  <div class="section-title" style="left:8px;top:892px;font-size:14px">Byte Lantern LLC<br>Blog Post</div>
  <div class="accent" role="img" aria-label="Wavy accent line" style="left:9px;top:964px;width:36px;height:4px"></div>
  <div class="section-text" style="left:66px;top:950px;font-size:8px;width:95px">Lorem ipsum dolor sit amet, consectetur adipiscing...</div>

  <div class="post" style="left:9px;top:1008px;width:98px;height:111px">
    <div class="post-img" role="img" aria-label="Photo of a businessman working on a laptop" style="height:82px;background:linear-gradient(135deg,#5b5450,#2b2b2d)"></div>
    <div class="post-date" style="left:10px;top:86px;font-size:5.5px">5 April, 2018</div>
    <div class="post-title" style="left:10px;top:96px;font-size:6.5px">Blog Post Write Here</div>
  </div>
  <div class="post" style="left:116px;top:1008px;width:98px;height:111px;border-bottom:3px solid var(--violet)">
    <div class="post-img" role="img" aria-label="Photo of a man in a suit outside glass towers" style="height:82px;background:linear-gradient(135deg,#a9d4ee,#3f74c9)"></div>
    <div class="post-date" style="left:10px;top:86px;font-size:5.5px">5 April, 2018</div>
    <div class="post-title" style="left:10px;top:96px;font-size:6.5px">Blog Post Write Here</div>
  </div>
  <div class="arrow" style="left:11px;top:1146px;width:14px;height:14px"></div>
  <div class="arrow" style="left:143px;top:1146px;width:14px;height:14px"></div>

  <div class="footer" style="top:1202px;height:541px">
    <div class="foot-head" style="left:13px;top:40px;font-size:10px">Get In Touch</div>
    <div class="field" style="left:13px;top:70px;width:140px;height:15px;font-size:7px">Name</div>
    <div class="field" style="left:13px;top:95px;width:140px;height:15px;font-size:7px">Email</div>
    <div class="field" style="left:13px;top:120px;width:140px;height:15px;font-size:7px">Phone No</div>
    <div class="field" style="left:13px;top:145px;width:140px;height:55px;font-size:7px">Message</div>
    <svg class="abs" style="left:142px;top:190px" width="10" height="9" viewBox="0 0 10 9"><path d="M0 5 L10 0 L7 9 L5 5 Z" fill="#e8322d"/></svg>
    <div class="foot-head" style="left:13px;top:251px;font-size:10px">Quick Links</div>
    <div class="foot-link" style="left:13px;top:281px;font-size:5.5px">Home</div>
    <div class="foot-link" style="left:45px;top:281px;font-size:5.5px">Our Services</div>
    <div class="foot-link" style="left:98px;top:281px;font-size:5.5px">About Us</div>
    <div class="foot-link" style="left:13px;top:295px;font-size:5.5px">Blogs</div>
    <div class="foot-link" style="left:45px;top:295px;font-size:5.5px">Contact Us</div>
    <div class="foot-head" style="left:13px;top:338px;font-size:10px">Others</div>
    <svg class="abs" style="left:13px;top:368px" width="9" height="7" viewBox="0 0 9 7"><rect x=".5" y=".5" width="8" height="6" fill="none" stroke="#fff"/><path d="M.5 .5 L4.5 4 L8.5 .5" fill="none" stroke="#fff"/></svg>
    <div class="foot-link" style="left:31px;top:367px;font-size:5.5px">info@bytelantern.com</div>
    <svg class="abs" style="left:13px;top:396px" width="8" height="10" viewBox="0 0 8 10"><path d="M4 9.5 C 1 6, .5 4.5, .5 3.5 A3.5 3.5 0 0 1 7.5 3.5 C 7.5 4.5, 7 6, 4 9.5Z" fill="none" stroke="#fff"/><circle cx="4" cy="3.5" r="1.2" fill="#fff"/></svg>
    <div class="foot-link" style="left:31px;top:395px;font-size:5.5px;width:110px;line-height:1.5">18 Harbor Lane, Fairview, CA, 90210, United States</div>
    <div class="round" style="left:13px;top:432px;width:11px;height:11px;background:#3b5bb8"></div>
    <div class="round" style="left:29px;top:432px;width:11px;height:11px;background:#2d9be0"></div>
    <div class="round" style="left:45px;top:432px;width:11px;height:11px;background:#c33a9a"></div>
    <div class="round" style="left:61px;top:432px;width:11px;height:11px;background:#2a73b8"></div>
    <div class="foot-bar" style="top:483px;height:58px">
      <div class="logo" style="left:0;width:167px;top:14px;font-size:6px;color:#fff;text-align:center">BYTE LANTERN</div>
      <div class="foot-link" style="left:0;width:167px;top:32px;font-size:6px;text-align:center">Copyright © 2020, byte lantern LLC</div>
    </div>
  </div>
</div>

<!-- desktop home page -->
<div class="site" style="left:375px;top:1045px;width:715px;height:1790px">
  <div class="nav" style="height:48px">
    <div class="logo" style="left:88px;top:16px;font-size:11px"><i style="width:10px;height:10px"></i>BYTE LANTERN</div>
    <div class="nav-link active" style="left:292px;top:19px">Home</div>
    <div class="nav-link" style="left:341px;top:19px">Services</div>
    <div class="nav-link" style="left:401px;top:19px">Blogs</div>
    <div class="social" style="left:563px;top:20px"></div>
    <div class="social" style="left:575px;top:20px"></div>
    <div class="mail-btn" style="left:611px;top:11px"></div>
  </div>
  <div class="hero" style="top:48px;height:368px">
    <div class="hero-title" style="left:88px;top:74px;font-size:48px">Welcome To<br>Byte Lantern LLC</div>
    <div class="accent light" role="img" aria-label="Wavy accent line" style="left:88px;top:218px;width:66px;height:6px"></div>
    <div class="hero-text" style="left:173px;top:204px;font-size:11.5px;width:460px;line-height:1.25">Lorem ipsum dolor sit amet, consectetur adipiscing elit, sed do eiusmod tempor incididunt ut labore et dolore magna aliqua.</div>
    <div class="btn" style="left:90px;top:264px;width:84px;height:26px;font-size:7px">Contact Us</div>
  </div>

  <div class="arrow" style="left:45px;top:497px;width:16px;height:16px"><svg viewBox="0 0 16 16"><path d="M10 8H5M7 5.5L4.5 8 7 10.5" fill="none" stroke="#fff" stroke-width="1.2"/></svg></div>
  <div class="partner" style="left:80px;top:496px;width:110px;font-size:14px">Streamline</div>
  <div class="partner-sep" style="left:215px;top:482px;height:46px"></div>
  <div class="partner" style="left:225px;top:496px;width:110px;font-size:14px">Flarecore</div>
  <div class="partner-sep" style="left:340px;top:482px;height:46px"></div>
  <div class="partner" style="left:350px;top:496px;width:140px;font-size:14px">Iceframe</div>
  <div class="partner-sep" style="left:490px;top:482px;height:46px"></div>
  <div class="partner" style="left:500px;top:496px;width:130px;font-size:14px">Pipeworks</div>
  <div class="arrow" style="left:652px;top:497px;width:16px;height:16px"><svg viewBox="0 0 16 16"><path d="M6 8h5M9 5.5L11.5 8 9 10.5" fill="none" stroke="#fff" stroke-width="1.2"/></svg></div>

  <div class="section-title" style="left:88px;top:618px;font-size:27px">Byte Lantern LLC<br>Services</div>
  <div class="accent" role="img" aria-label="Wavy accent line" style="left:88px;top:734px;width:52px;height:5px"></div>
  <div class="section-text" style="left:151px;top:716px;font-size:13px;width:190px">Lorem ipsum dolor sit amet, consectetur adipiscing...</div>

  <div class="card" style="left:360px;top:595px;width:258px;height:188px">
    <div class="card-icon" role="img" aria-label="Platform architecture blueprint illustration" style="left:35px;top:20px;width:68px;height:68px"></div>
    <div class="card-title" style="left:35px;top:115px;font-size:14px">Platform Architecture</div>
    <div class="card-text" style="left:35px;top:143px;font-size:7.5px;width:180px">Byte Lantern works very closely with clients, product...</div>
  </div>
  <div class="card" style="left:88px;top:798px;width:258px;height:190px">
    <div class="card-icon" role="img" aria-label="Data engineering chip illustration" style="left:35px;top:20px;width:68px;height:68px"></div>
    <div class="card-title" style="left:35px;top:118px;font-size:14px">Data Engineering</div>
    <div class="card-text" style="left:35px;top:146px;font-size:7.5px;width:180px">Byte Lantern works very closely with clients, product...</div>
  </div>
  <div class="card" style="left:360px;top:798px;width:258px;height:190px">
    <div class="card-icon" role="img" aria-label="Cloud development illustration" style="left:35px;top:20px;width:62px;height:68px"></div>
    <div class="card-title" style="left:35px;top:118px;font-size:14px">Cloud Development</div>
    <div class="card-text" style="left:35px;top:146px;font-size:7.5px;width:180px">Byte Lantern works very closely with clients, product...</div>
  </div>

  <div class="section-title" style="left:88px;top:1045px;font-size:27px">Byte Lantern LLC<br>Blog Posts</div>
  <div class="accent" role="img" aria-label="Wavy accent line" style="left:88px;top:1160px;width:52px;height:5px"></div>
  <div class="section-text" style="left:151px;top:1142px;font-size:13px;width:190px">Lorem ipsum dolor sit amet, consectetur adipiscing...</div>
  <div class="arrow" style="left:550px;top:1098px;width:28px;height:28px"><svg viewBox="0 0 28 28"><path d="M18 14H10M13 10.5L9.5 14 13 17.5" fill="none" stroke="#fff" stroke-width="1.5"/></svg></div>
  <div class="arrow" style="left:596px;top:1098px;width:28px;height:28px"><svg viewBox="0 0 28 28"><path d="M10 14h8M15 10.5L18.5 14 15 17.5" fill="none" stroke="#fff" stroke-width="1.5"/></svg></div>

  <div class="post" style="left:88px;top:1210px;width:170px;height:192px">
    <div class="post-img" role="img" aria-label="Photo of a businessman working on a laptop" style="height:142px;background:linear-gradient(135deg,#6a625c,#2a2a2c)"></div>
    <div class="post-date" style="left:19px;top:157px;font-size:7px">5 April, 2018</div>
    <div class="post-title" style="left:19px;top:170px;font-size:12.5px">Blog Post Write Here</div>
  </div>
  <div class="post" style="left:271px;top:1210px;width:170px;height:192px;border-bottom:3px solid var(--blue)">
    <div class="post-img" role="img" aria-label="Photo of a man in a blue suit outside glass towers" style="height:142px;background:linear-gradient(135deg,#b5dcf2,#3c6ec4)"></div>
    <div class="post-date" style="left:19px;top:157px;font-size:7px">5 April, 2018</div>
    <div class="post-title" style="left:19px;top:170px;font-size:12.5px">Blog Post Write Here</div>
  </div>
  <div class="post" style="left:455px;top:1210px;width:170px;height:192px">
    <div class="post-img" role="img" aria-label="Photo of a city skyline seen through office windows" style="height:142px;background:linear-gradient(135deg,#aab8c6,#4f5c6b)"></div>
    <div class="post-date" style="left:19px;top:157px;font-size:7px">5 April, 2018</div>
    <div class="post-title" style="left:19px;top:170px;font-size:12.5px">Blog Post Write Here</div>
  </div>
  <div class="post" style="left:638px;top:1210px;width:170px;height:192px">
    <div class="post-img" role="img" aria-label="Photo of a man working on a laptop" style="height:142px;background:linear-gradient(135deg,#c9d3dd,#6f7f93)"></div>
    <div class="post-date" style="left:19px;top:157px;font-size:7px">5 April, 2018</div>
    <div class="post-title" style="left:19px;top:170px;font-size:12.5px">Blog Post Write Here</div>
  </div>

  <div class="footer" style="top:1475px;height:315px">
    <div class="foot-head" style="left:88px;top:45px;font-size:12px">Quick Links</div>
    <div class="foot-link" style="left:88px;top:88px;font-size:7.5px">Home</div>
    <div class="foot-link" style="left:88px;top:106px;font-size:7.5px">Our Services</div>
    <div class="foot-link" style="left:88px;top:124px;font-size:7.5px">About Us</div>
    <div class="foot-link" style="left:88px;top:142px;font-size:7.5px">Blogs</div>
    <div class="foot-link" style="left:88px;top:160px;font-size:7.5px">Contact Us</div>
    <div class="foot-head" style="left:242px;top:45px;font-size:12px">Others</div>
    <svg class="abs" style="left:242px;top:88px" width="10" height="8" viewBox="0 0 10 8"><rect x=".5" y=".5" width="9" height="7" fill="none" stroke="#fff"/><path d="M.5 .5 L5 4.5 L9.5 .5" fill="none" stroke="#fff"/></svg>
    <div class="foot-link" style="left:260px;top:86px;font-size:7.5px">info@bytelantern.com</div>
    <svg class="abs" style="left:242px;top:119px" width="9" height="11" viewBox="0 0 8 10"><path d="M4 9.5 C 1 6, .5 4.5, .5 3.5 A3.5 3.5 0 0 1 7.5 3.5 C 7.5 4.5, 7 6, 4 9.5Z" fill="none" stroke="#fff"/><circle cx="4" cy="3.5" r="1.2" fill="#fff"/></svg>
    <div class="foot-link" style="left:260px;top:117px;font-size:7.5px;width:115px;line-height:1.5">18 Harbor Lane, Fairview, CA, 90210, United States</div>
    <div class="round" style="left:242px;top:188px;width:14px;height:14px;background:#3b5bb8"></div>
    <div class="round" style="left:262px;top:188px;width:14px;height:14px;background:#2d9be0"></div>
    <div class="round" style="left:282px;top:188px;width:14px;height:14px;background:#c33a9a"></div>
    <div class="round" style="left:302px;top:188px;width:14px;height:14px;background:#2a73b8"></div>
    <div class="foot-head" style="left:421px;top:45px;font-size:12px">Get In Touch</div>
    <div class="field" style="left:421px;top:84px;width:204px;height:15px;font-size:7.5px">Name</div>
    <div class="field" style="left:421px;top:109px;width:204px;height:15px;font-size:7.5px">Email</div>
    <div class="field" style="left:421px;top:134px;width:204px;height:15px;font-size:7.5px">Phone No</div>
    <div class="field" style="left:421px;top:159px;width:204px;height:64px;font-size:7.5px">Message</div>
    <svg class="abs" style="left:608px;top:203px" width="15" height="14" viewBox="0 0 10 9"><path d="M0 5 L10 0 L7 9 L5 5 Z" fill="#e8322d"/></svg>
    <div class="foot-bar" style="top:275px;height:40px">
      <div class="logo" style="left:88px;top:13px;font-size:9px;color:#fff"><i style="width:8px;height:8px"></i>BYTE LANTERN</div>
      <div class="foot-link" style="left:440px;width:185px;top:14px;font-size:7.5px;text-align:right">Copyright © 2020, byte lantern LLC</div>
    </div>
  </div>
</div>

</body>
</html>
```